Stationery Design Project

Fire and building compliance company needs business card, letterhead and complement slip designed.
Have included a brief about business card, basic want front keep quite clean with just the KTW logo and the words Marloway Alarm and Safety 2012 Ltd (small print) along the bottom. Website needs to be included (www.ktwalarm.example.nz) on either front or back.
The info for back is as per attachment.
Letterhead and complement slip should have the usual stuff KTW logo etc and also the accredited test lab logo at the bottom (can be small size)
Target Market(s)
Property owners, buisness managers
Industry/Entity Type
Building
Look and feel
Each slider illustrates characteristics of the customer's brand and the style your logo design should communicate.

```html
<!DOCTYPE html>
<html lang="en">
<head>
<meta charset="utf-8">
<title>KTW – With Compliments Slip</title>
<link rel="stylesheet" href="https://fonts.googleapis.com/css2?family=Open+Sans:wght@400;600&family=Caveat:wght@400&display=swap">
<style>
  :root {
    --paper: #ffffff;
    --ink-dark: #3d3d3d;
    --ink-text: #333333;
    --flame: #f07a2a;
    --wash-warm: #f6c9b0;
    --wash-cool: #bcd9e8;
  }
  html, body {
    margin: 0;
    padding: 0;
    overflow: hidden;
    background: var(--paper);
  }
  .slip {
    position: relative;
    width: 1200px;
    height: 600px;
    background: var(--paper);
    overflow: hidden;
    font-family: "Open Sans", Arial, sans-serif;
  }
  .slip__backdrop {
    position: absolute;
    left: 600px;
    top: -40px;
    width: 640px;
    height: 640px;
    border-radius: 50%;
    background: radial-gradient(circle at 40% 40%, var(--wash-warm) 0%, var(--wash-cool) 100%);
    opacity: 0.25;
  }
  .brand {
    position: absolute;
    left: 28px;
    top: 40px;
    display: flex;
    align-items: center;
    gap: 22px;
  }
  .brand__dot {
    width: 110px;
    height: 110px;
    border-radius: 50%;
    background: var(--flame);
  }
  .brand__name {
    font-weight: 600;
    font-size: 76px;
    line-height: 1;
    letter-spacing: 1px;
    color: var(--ink-dark);
  }
  .greeting {
    position: absolute;
    left: 130px;
    top: 536px;
    margin: 0;
    font-family: "Caveat", cursive;
    font-size: 42px;
    font-weight: 400;
    color: var(--ink-dark);
    line-height: 1;
  }
  .contact {
    position: absolute;
    left: 632px;
    top: 573px;
    margin: 0;
    font-size: 10.5px;
    color: var(--ink-text);
    white-space: nowrap;
  }
</style>
</head>
<body>
  <main class="slip">
    <div class="slip__backdrop" aria-hidden="true"></div>

    <header class="brand">
      <span class="brand__dot" aria-hidden="true"></span>
      <span class="brand__name">KTW</span>
    </header>

    <p class="greeting">With Compliments</p>

    <address class="contact">18 Harbour View Road, Riverton, 4510 - Phone: 06 555 0142 - Fax: 06 555 0187 - Email: admin@marloway.example.nz</address>
  </main>
</body>
</html>
```